Stunning website design for world's unique software

Design only (No coding required)
This website design is linked with a logo design and illustration design contests.

Industry/Entity Type

Software

```html
<!DOCTYPE html>
<html lang="en">
<head>
<meta charset="utf-8">
<title>spanlink — Easy Multimedia Control</title>
<link href="https://fonts.googleapis.com/css2?family=Arimo:wght@400;700&display=swap" rel="stylesheet">
<style>
:root{
  --orange:#f7931e;
  --orange-deep:#f26b1d;
  --ink:#1a1a1a;
  --text:#555;
  --band:#dcdcdc;
  --hero:#efefef;
  --row-dark:#bdbdbd;
  --row-light:#e9e9e9;
  --notes:#f0f0f0;
  --white:#fff;
  --icon-blue:#2a70bd;
  --icon-grey:#8a8a8a;
}
*{box-sizing:border-box;margin:0;padding:0}
html,body{width:1200px;height:1000px;overflow:hidden;background:#e4e4e4;font-family:"Arimo",Arial,sans-serif;color:var(--text)}
.abs{position:absolute}
.sq{display:inline-block;background:var(--orange)}
/* ---------- overview column ---------- */
.overview{position:absolute;left:0;top:0;width:345px;height:1000px;background:var(--white);overflow:hidden;border-right:1px solid #ccc}
.ov-header{height:20px;display:flex;align-items:center;padding:0 46px;gap:4px}
.ov-brand{font-weight:700;font-size:11px;color:var(--ink);display:flex;align-items:center;gap:3px}
.ov-nav{margin-left:auto;display:flex;gap:7px;font-size:5px;color:#444}
.ov-nav span:first-child{color:var(--orange)}
.ov-hero{position:absolute;top:20px;left:0;width:345px;height:142px;background:var(--hero);text-align:center}
.ov-hero h2{font-weight:400;color:var(--orange);font-size:10px;margin-top:10px}
.ov-hero p{font-size:5px;width:200px;margin:2px auto 0;line-height:1.3}
.ov-icons{position:absolute;top:162px;width:345px;height:46px;background:var(--band)}
.tiny{font-size:4.5px;line-height:1.35;color:#555}
.tiny-b{font-size:5px;font-weight:700;color:#333}
.ov-row{background:var(--row-dark);height:12px;font-size:4.5px;padding:3px 3px;color:#333}
.ov-cell{background:var(--row-light);font-size:4px;padding:3px;color:#444}
.ov-bar{position:absolute;top:410px;width:345px;height:25px;background:var(--orange-deep);color:#fff;font-size:9px;display:flex;align-items:center;padding-left:50px;gap:3px}
.ov-h{font-weight:700;color:var(--orange-deep);font-size:11px;line-height:1.2}
.ov-h-dark{font-weight:700;color:#333;font-size:11px;line-height:1.15}
.dot{display:inline-block;width:5px;height:5px;background:var(--orange);transform:rotate(45deg);margin-right:4px}
.shot{background:#d6d9de;border:1px solid #bbb}
/* ---------- detail panel ---------- */
.detail{position:absolute;left:345px;top:0;width:855px;height:1000px;background:var(--white);overflow:hidden}
.site-header{height:65px;position:relative}
.brand{position:absolute;left:118px;top:12px;display:flex;align-items:center;gap:8px;font-weight:700;font-size:30px;color:var(--ink);letter-spacing:-.5px}
.nav{position:absolute;left:403px;top:18px;display:flex;gap:20px;font-size:11px;color:#444}
.nav .current{color:var(--orange)}
.hero{position:absolute;top:65px;left:0;width:855px;height:340px;background:linear-gradient(#e8e8e8,#f6f6f6 40%,#fafafa)}
.hero h1{font-weight:400;font-size:22px;color:var(--orange);text-align:center;margin-top:14px}
.hero p{font-size:11px;text-align:center;width:420px;margin:6px auto 0;line-height:1.35;color:#666}
.hero-art{position:absolute;left:150px;top:85px;width:580px;height:230px;background:radial-gradient(ellipse at 50% 60%,#f6b27a 0%,#f3d8e6 45%,#f4f2f2 80%);border-radius:4px}
.feature-band{position:absolute;top:405px;width:855px;height:115px;background:var(--band)}
.notch{position:absolute;left:412px;top:-10px;width:0;height:0;border-left:12px solid transparent;border-right:12px solid transparent;border-bottom:10px solid var(--band)}
.feature{position:absolute;top:12px;width:180px;text-align:center;font-size:11px;color:#666;white-space:nowrap}
.feature .icon{display:block;width:76px;height:74px;margin:0 auto 11px;border-radius:8px}
.icon-blue{background:linear-gradient(var(--icon-blue),#1f5fa3)}
.icon-grey{background:linear-gradient(#9a9a9a,#6f6f6f)}
.env{position:absolute;top:520px;width:855px;height:356px}
.env-mark{position:absolute;left:0;width:855px;top:20px;display:flex;justify-content:center;align-items:center;gap:7px;color:#aaa;font-weight:700;font-size:27px}
.env h2{position:absolute;top:68px;width:855px;text-align:center;font-size:21px;font-weight:700;color:var(--ink)}
.col{position:absolute;top:120px;width:278px}
.col h3{text-align:center;font-size:14px;font-weight:700;color:var(--ink);margin-bottom:6px}
.acc{background:var(--row-dark);height:33px;font-size:11px;color:#333;padding:10px 12px;margin-top:5px}
.acc.first{margin-top:0}
.acc-body{background:var(--row-light);font-size:9.3px;color:#333;padding:6px 12px;line-height:1.25}
.acc-body ol{padding-left:14px}
.acc-body li{margin-bottom:8px}
.notes{position:absolute;top:876px;width:855px;height:124px;background:var(--notes)}
.notes h4{text-align:center;font-weight:400;font-size:16px;color:#444;margin-top:10px}
.notes ol{font-size:9.2px;color:#333;line-height:1.15;margin:5px 0 0 120px;padding-left:30px;width:620px}
</style>
</head>
<body>

<section class="overview" aria-label="Full page overview">
  <div class="ov-header">
    <span class="ov-brand"><span class="sq" style="width:9px;height:9px"></span>spanlink</span>
    <nav class="ov-nav"><span>spanlink?</span><span>Download</span><span>Buy Now</span><span>Manual</span><span>Support</span><span>Forum</span></nav>
  </div>
  <div class="ov-hero">
    <h2>World's BlueLink Unique HID Emulator</h2>
    <p>spanlink makes BlueLink controller equipped PC or Orchard computer work as a standard BlueLink keyboard/mouse combo. So you can seamlessly control all your smart devices including computer, smartphone and tablet PC with the computer's keyboard and mouse.</p>
    <div role="img" aria-label="Illustration of tablet, phone, computer and laptop connected by wireless waves" class="abs" style="left:50px;top:50px;width:225px;height:88px;background:radial-gradient(ellipse,#f7a65c,#e3e3e3 75%)"></div>
  </div>
  <div class="ov-icons">
    <div role="img" aria-label="Keyboard and mouse icon" class="abs" style="left:74px;top:5px;width:24px;height:26px;background:var(--icon-blue);border-radius:3px"></div>
    <div role="img" aria-label="Multimedia controller icon" class="abs" style="left:158px;top:5px;width:24px;height:26px;background:var(--icon-grey);border-radius:3px"></div>
    <div role="img" aria-label="Text copy icon" class="abs" style="left:244px;top:5px;width:24px;height:26px;background:var(--icon-blue);border-radius:3px"></div>
    <div class="tiny abs" style="left:60px;top:36px">BlueLink Keyboard + Mouse</div>
    <div class="tiny abs" style="left:150px;top:36px">Multimedia Controller</div>
    <div class="tiny abs" style="left:240px;top:36px">Useful Textcopy</div>
  </div>
  <div class="abs" style="top:216px;left:0;width:345px;text-align:center">
    <div style="color:#aaa;font-weight:700;font-size:10px;display:flex;justify-content:center;align-items:center;gap:3px"><span class="sq" style="width:8px;height:8px;background:#bbb"></span>spanlink</div>
    <div style="font-weight:700;font-size:8px;color:#222;margin-top:8px">Operation Environtment</div>
  </div>
  <div class="abs" style="left:54px;top:256px;width:110px">
    <div class="tiny-b" style="text-align:center;margin-bottom:3px">spanlink Server</div>
    <div class="ov-row">- Summary</div>
    <div class="ov-cell">Main program running on a computer whose keyboard and mouse are used to control your client devices.</div>
    <div class="ov-row" style="margin-top:3px">+ Function</div>
    <div class="ov-row" style="margin-top:3px">- OS Requirement</div>
    <div class="ov-cell"><b>32&amp;64-bit Panes 7,8,Summit<br>Orchard OS 10.6 and later</b></div>
  </div>
  <div class="abs" style="left:180px;top:256px;width:112px">
    <div class="tiny-b" style="text-align:center;margin-bottom:3px">spanlink Client</div>
    <div class="ov-row">+ Summary</div>
    <div class="ov-row" style="margin-top:3px">- Function</div>
    <div class="ov-cell">1. Mouse cursor moves back and forth between dual monitors or devices.<br>2. It enables you copy texts between devices using copy and paste.</div>
    <div class="ov-row" style="margin-top:3px">+ OS Requirement</div>
  </div>
  <div class="abs" style="top:352px;left:0;width:345px;height:58px;background:var(--notes)">
    <div style="text-align:center;font-size:7px;color:#444;margin-top:3px">Notes:</div>
    <div class="tiny" style="margin:2px 0 0 56px;width:240px;font-size:3.8px">1. <b>Even though spanlink client is not installed on your client device,</b> the keyboard or mouse hotkey still controls the client device.<br>2. On Panes 7,8,Summit and Orchard OS 10.6 and later, you can switch between Server and Client mode.<br>3. Orchard Mobile does not support a BlueLink mouse; keyboard works well.<br>4. For Panes, only the Panes BlueLink stack is supported.</div>
  </div>
  <div class="ov-bar"><span class="sq" style="width:8px;height:8px;background:#fff"></span><b>spanlink</b>&nbsp;Features</div>
  <div class="abs" style="top:435px;left:0;width:345px;height:110px;background:#f4f4f4">
    <div class="ov-h abs" style="left:50px;top:8px">Super easy to<br>setup and use.</div>
    <div class="abs tiny" style="left:66px;top:40px;width:105px"><span class="dot"></span><b style="font-size:5.5px">Intuitive UX/UI</b><br>Excellent UX/UI design makes setup easy.<br><br><span class="dot"></span><b style="font-size:5.5px">Same experience on PC and Orchard</b><br>Identical experience on both systems.<br><br><span class="dot"></span><b style="font-size:5.5px">17 languages supported</b><br>English, German, French, ... supported</div>
    <div role="img" aria-label="Software settings window screenshots" class="shot abs" style="left:175px;top:6px;width:122px;height:96px"></div>
  </div>
  <div class="abs" style="top:545px;left:0;width:345px;height:140px;background:#dedede">
    <div class="ov-h-dark abs" style="left:50px;top:10px">Simultaneous<br>control of<br>multiple<br>client devices</div>
    <div role="img" aria-label="Pairing window screenshot" class="shot abs" style="left:137px;top:13px;width:73px;height:80px;background:#f4f4f4"></div>
    <div role="img" aria-label="Client devices layout screenshot" class="shot abs" style="left:218px;top:13px;width:73px;height:80px;background:#f4f4f4"></div>
    <div class="abs tiny" style="left:137px;top:97px;width:73px"><b>Pairing available up to 6 devices</b><br>You can do pairing up to 6 client devices.</div>
    <div class="abs tiny" style="left:218px;top:97px;width:75px"><b>Simultaneously controllable up to 4 devices</b><br>Control up to 4 client devices by placing each one.</div>
  </div>
  <div class="abs" style="top:685px;left:0;width:345px;height:136px;background:#fff">
    <div class="ov-h-dark abs" style="left:50px;top:6px;width:250px">Pairing with multiple spanlink Servers on your client device</div>
    <div class="abs tiny" style="left:50px;top:36px;width:250px;font-size:5px">For example, you can make your smartphone BlueLink pairing with your home and office computer, and you can use one of them by selecting it at home or office.</div>
    <div role="img" aria-label="Illustration of a phone paired with two computers" class="abs" style="left:90px;top:56px;width:165px;height:78px;background:radial-gradient(ellipse,#f4a15a,#efefef 75%)"></div>
  </div>
  <div class="abs" style="top:821px;left:46px;width:252px;height:145px;display:grid;grid-template-columns:repeat(3,1fr);grid-template-rows:1fr 1fr;gap:2px;background:#fff">
    <div style="background:#eee;padding:4px"><div class="tiny-b" style="font-size:7px">Your BlueLink gadgets not affected</div><div class="tiny" style="font-size:3.8px">Existing BlueLink gadgets keep working without worry.</div></div>
    <div style="background:#ddd;padding:4px"><div class="tiny-b" style="font-size:7px">Natural and stable experience</div><div class="tiny" style="font-size:3.8px">Works as natural as your own keyboard and mouse.</div></div>
    <div style="background:#eee;padding:4px"><div class="tiny-b" style="font-size:7px">Any type of keyboard and mouse supported</div><div class="tiny" style="font-size:3.8px">Wired or wireless, any type can be used.</div></div>
    <div style="background:#eee;padding:4px"><div class="tiny-b" style="font-size:7px">Convenient multimedia control</div><div class="tiny" style="font-size:3.8px">Send volume and playback keys to devices.</div></div>
    <div style="background:#ccc;padding:4px;grid-column:span 2"><div class="tiny-b" style="font-size:7px;margin-left:60px">Multi-monitor supported completely</div><div class="tiny" style="font-size:3.8px;margin-left:60px">Full multi-monitor environment support.</div></div>
  </div>
  <div class="abs" style="top:966px;left:0;width:345px;height:34px;background:#d4d4d4">
    <div style="position:absolute;right:50px;top:4px;color:#fff;font-weight:700;font-size:10px;display:flex;align-items:center;gap:3px"><span class="sq" style="width:8px;height:8px;background:#fff"></span>spanlink</div>
    <div class="tiny" style="position:absolute;left:0;width:345px;bottom:3px;text-align:center;font-size:3.5px">Copyright 2013 spanlink. All rights reserved.</div>
  </div>
</section>

<main class="detail">
  <header class="site-header">
    <div class="brand"><span class="sq" style="width:24px;height:24px"></span>spanlink</div>
    <nav class="nav"><span class="current">spanlink?</span><span>Download</span><span>Buy Now</span><span>Manual</span><span>Support</span><span>Forum</span></nav>
  </header>

  <section class="hero">
    <h1>Easy Multimedia Control</h1>
    <p>spanlink lets you comfortably input multimedia keys (Volume Up/Down, Mute, ...) to your smart devices.</p>
    <div class="hero-art" role="img" aria-label="Illustration: tablet, phone, desktop with a Multimedia Keys window and laptop, with colored arrows linking volume, mute and play keys to each device, over floating music notes"></div>
  </section>

  <section class="feature-band">
    <div class="notch"></div>
    <div class="feature" style="left:127px">
      <div class="icon icon-blue" role="img" aria-label="Wireless keyboard and mouse icon"></div>
      BlueLink Keyboard + Mouse
    </div>
    <div class="feature" style="left:337px">
      <div class="icon icon-grey" role="img" aria-label="Multimedia controller icon"></div>
      Multimedia Controller
    </div>
    <div class="feature" style="left:550px">
      <div class="icon icon-blue" role="img" aria-label="Text copy icon"></div>
      Useful Textcopy
    </div>
  </section>

  <section class="env">
    <div class="env-mark"><span class="sq" style="width:24px;height:24px;background:#bbb"></span>spanlink</div>
    <h2>Operation Environtment</h2>
    <div class="col" style="left:132px">
      <h3>spanlink Server</h3>
      <div class="acc first">-&nbsp; Summary</div>
      <div class="acc-body">Main program running on a computer whose keyboard and mouse are used to control your client devices.</div>
      <div class="acc">+ Function</div>
      <div class="acc">- OS Requirement</div>
      <div class="acc-body" style="height:62px;padding-top:9px"><b>32&amp;64-bit Panes 7,8,Summit<br>Orchard OS 10.6 and later</b></div>
    </div>
    <div class="col" style="left:448px">
      <h3>spanlink Client</h3>
      <div class="acc first">+ Summary</div>
      <div class="acc">-&nbsp; Function</div>
      <div class="acc-body"><ol><li>Mouse cursor moves back and forth between dual monitors of a computer. Similarly, spanlink Client enables the mouse cursor move back and forth between an spanlink Server computer and a client device.</li><li style="margin-bottom:2px">It enables you copy texts between devices using normal copy and paste.</li></ol></div>
      <div class="acc">+ OS Requirement</div>
    </div>
  </section>

  <section class="notes">
    <h4>Notes:</h4>
    <ol>
      <li><b>Even though spanlink client is not installed on your client device,</b> , the keyboard or mouse hotkey enables you control the client device using the spanlink Server computer's keyboard and mouse. In this case, just the two functions (mouse-dragging and text-copy between devices) provided by spanlink Client is not available.</li>
      <li>On Panes 7,8,Summit, and Orchard OS 10.6 and later, you can switch the spanlink software mode between spanlink Server and spanlink Client. On Panes Classic and Droidline, spanlink Client only works.</li>
      <li>Orchard Mobile does not support a BlueLink mouse. Therefore, mouse operation does not work on an Orchard phone or Orchard tablet while keyboard works well on an Orchard Mobile device.</li>
      <li>For Panes, only Panes BlueLink stack is supported; Other BlueLink stacks (Tosaki, Bluesun, ...) are not supported</li>
    </ol>
  </section>
</main>
</body>
</html>
```